truck and trailer business Wrap Design

needing a redisgn of our truck and trailer wraps, i have attached the current trailer wrap design and pictures of the new trailer needing a wrap design. trailer is 26ft v nose. 8.5 wide and 7.5ft tall need the trucks that pull the trailers to match. 2018 r-380 long bed. i have attached pictures of the truck. 2009 ZOBI 26 FT BOX
Updates

Low design quality

Industry/Entity Type

Insulation

Colors

Designer to choose colors to be used in the design.

Requirements
Must have
• wrap needs to be unique and stand out like our current wrap

```html
<!DOCTYPE html>
<html lang="en">
<head>
<meta charset="utf-8">
<title>Summit Spray Foam – Trailer and Truck Wrap Layouts</title>
<link href="https://fonts.googleapis.com/css2?family=Lato:ital,wght@0,400;0,700;0,900;1,700&display=swap" rel="stylesheet">
<style>
  :root {
    --stage-light: #cfd0d2;
    --stage-dark: #3b3b3d;
    --panel-black: #121214;
    --panel-charcoal: #2a2a2d;
    --photo-foam: #e9e4d8;
    --photo-wood: #c8a06a;
    --photo-batt: #d9b87a;
    --photo-suit: #dfe3e8;
    --ink-white: #ffffff;
    --rule-white: #f2f2f2;
    --shadow: rgba(0,0,0,0.45);
  }
  * { margin: 0; padding: 0; box-sizing: border-box; }
  html, body { width: 1200px; height: 566px; overflow: hidden; }
  body {
    position: relative;
    font-family: 'Lato', Arial, sans-serif;
    background: linear-gradient(to bottom, var(--stage-light) 0 432px, var(--stage-dark) 432px 566px);
  }
  .wrap-panel {
    position: absolute;
    overflow: hidden;
    box-shadow: 3px 5px 8px var(--shadow);
    background: var(--panel-black);
  }
  .trailer-side { left: 32px; width: 830px; height: 240px; }
  .trailer-side--upper { top: 32px; }
  .trailer-side--lower { top: 293px; }
  .truck-door { left: 896px; top: 163px; width: 272px; height: 238px; }

  .photo-area { position: absolute; }
  .photo-area--attic {
    background: linear-gradient(135deg, var(--photo-batt) 0%, var(--photo-wood) 45%, var(--photo-foam) 70%, var(--photo-suit) 100%);
  }
  .photo-area--spray {
    background: linear-gradient(160deg, var(--photo-foam) 0%, var(--photo-wood) 50%, var(--photo-suit) 100%);
  }
  .panel-shape { position: absolute; inset: 0; width: 100%; height: 100%; }

  .panel-copy {
    position: absolute;
    top: 0;
    color: var(--ink-white);
    text-align: center;
  }
  .service-list { font-weight: 900; font-size: 17px; letter-spacing: 0.2px; white-space: nowrap; }
  .name-block {
    border-top: 2px solid var(--rule-white);
    border-bottom: 2px solid var(--rule-white);
    margin-top: 10px;
    padding: 6px 0 4px;
  }
  .brand-name {
    font-weight: 900;
    font-size: 32px;
    line-height: 30px;
    letter-spacing: 1px;
    color: var(--ink-white);
  }
  .web-address { font-weight: 900; font-size: 17px; margin-top: 14px; }
  .phone-number { font-weight: 900; font-size: 34px; line-height: 36px; }
  .social-line {
    display: flex; align-items: center; justify-content: center; gap: 5px;
    font-weight: 700; font-size: 7px; margin-top: 12px; white-space: nowrap;
  }
  .social-dot { width: 13px; height: 13px; border-radius: 50%; background: var(--ink-white); }

  .trailer-side--upper .panel-copy { left: 224px; width: 350px; padding-top: 30px; }
  .trailer-side--lower .panel-copy { left: 269px; width: 350px; padding-top: 30px; }

  .door-copy { position: absolute; left: 14px; top: 40px; width: 176px; color: var(--ink-white); }
  .door-tagline { font-weight: 900; font-size: 12px; line-height: 15px; }
  .door-name {
    margin-top: 28px;
    border-top: 1px solid var(--rule-white);
    border-bottom: 1px solid var(--rule-white);
    padding: 3px 0 2px;
    font-weight: 900; font-size: 12px; line-height: 12px; text-align: center; letter-spacing: 0.5px;
  }
  .door-web { font-weight: 900; font-size: 7px; margin-top: 22px; }
  .door-phone { font-weight: 900; font-size: 13px; line-height: 15px; }
  .door-social { display: flex; align-items: center; gap: 4px; font-weight: 700; font-size: 6px; margin-top: 14px; }
  .door-social .social-dot { width: 11px; height: 11px; }
</style>
</head>
<body>

<section class="wrap-panel trailer-side trailer-side--upper">
  <div class="photo-area photo-area--spray" style="left:0;top:0;width:220px;height:240px" role="img" aria-label="Photos of a worker trimming spray foam and a worker in protective suit spraying insulation"></div>
  <div class="photo-area photo-area--attic" style="left:620px;top:0;width:210px;height:240px" role="img" aria-label="Photos of attic fiberglass batts and a worker spraying foam between wall studs"></div>
  <svg class="panel-shape" viewBox="0 0 830 240" preserveAspectRatio="none" aria-hidden="true">
    <path d="M140,0 L700,0 Q650,120 705,240 L200,240 Q120,130 140,0 Z" fill="var(--panel-black)"/>
    <path d="M200,240 Q150,160 170,60 L190,240 Z" fill="var(--panel-charcoal)" opacity="0.6"/>
  </svg>
  <div class="panel-copy">
    <p class="service-list">SPRAY FOAM ● FIBERGLASS ● INSULATION ● ROOFING</p>
    <div class="name-block"><p class="brand-name">SUMMIT<br>SPRAY FOAM</p></div>
    <p class="web-address">SUMMITSPRAYFOAM.NET</p>
    <p class="phone-number">469-555-0142</p>
    <p class="social-line"><span class="social-dot"></span>SUMMITSPRAYFOAM | DFW PREMIER INSULATION COMPANY</p>
  </div>
</section>

<section class="wrap-panel trailer-side trailer-side--lower">
  <div class="photo-area photo-area--attic" style="left:0;top:0;width:230px;height:240px" role="img" aria-label="Photos of attic fiberglass batts and a worker spraying foam between wall studs"></div>
  <div class="photo-area photo-area--spray" style="left:660px;top:0;width:170px;height:240px" role="img" aria-label="Photos of a worker trimming spray foam and a worker in protective suit spraying insulation"></div>
  <svg class="panel-shape" viewBox="0 0 830 240" preserveAspectRatio="none" aria-hidden="true">
    <path d="M250,0 L725,0 Q790,120 730,240 L170,240 Q215,120 250,0 Z" fill="var(--panel-black)"/>
  </svg>
  <div class="panel-copy">
    <p class="service-list">SPRAY FOAM ● FIBERGLASS ● INSULATION ● ROOFING</p>
    <div class="name-block"><p class="brand-name">SUMMIT<br>SPRAY FOAM</p></div>
    <p class="web-address">SUMMITSPRAYFOAM.NET</p>
    <p class="phone-number">469-555-0142</p>
    <p class="social-line"><span class="social-dot"></span>SUMMITSPRAYFOAM | DFW PREMIER INSULATION COMPANY</p>
  </div>
</section>

<section class="wrap-panel truck-door">
  <div class="photo-area photo-area--spray" style="left:190px;top:0;width:82px;height:238px" role="img" aria-label="Photos of workers in protective suits spraying foam insulation"></div>
  <svg class="panel-shape" viewBox="0 0 272 238" preserveAspectRatio="none" aria-hidden="true">
    <path d="M0,0 L200,0 Q175,120 215,238 L0,238 Z" fill="var(--panel-black)"/>
  </svg>
  <div class="door-copy">
    <p class="door-tagline">DFW PREMIER<br>INSULATION COMPANY</p>
    <p class="door-name">SUMMIT SPRAY FOAM</p>
    <p class="door-web">SUMMITSPRAYFOAM.NET</p>
    <p class="door-phone">469-555-0142</p>
    <p class="door-social"><span class="social-dot"></span>SUMMITSPRAYFOAM</p>
  </div>
</section>

</body>
</html>
```